Design eines Hausetiketts für traditionelles Weingut
Zielgruppe
Wir das Familienweingut Brunnhofer in Gimbsheim/Rheinhessen sind ein traditionelles Weingut das seine Reben selbst kultiviert und die Weine auch selbst ausbaut. Wir haben jeden Schritt in der Weinherstellung selbst in der Hand und vermarkten den Wein dann an unsere Privatkunden. Unsere Kundenstruktur sieht folgendermaßen aus: Wir haben 100% Privatkunden die unseren Wein konsumieren. Da jetzt die nächste Generation in den Weinbaubetrieb einsteigt und auch Ideen hat möchten wir ein Hausetikett einführen. Im Moment haben wir noch sehr viele unterschiedliche Etiketten und kein Hausetikett. Da die Verlagsetiketten immer seltener zu unseren Vorstellungen passen, möchten wir hier auf diesem Wege ein Hausetikett anfertigen lassen. Generell möchten wir unseren Außenauftritt komplett modernisieren. Sie können sich über die Vielfalt in unserem Betrieb unter www.weingut-brunnhofer-beispiel.de einen Überblick verschaffen. Langfristig gesehen wollen wir aber unsere Weinkarte verkleinern.
Aufgabenstellung
Wir haben uns vor ca. 1,5 Jahren hier auf dieser Website bereits ein Logo designen lassen. Es wäre schön wenn man das Logo bei den Entwürfen für die Etiketten berücksichtigen würde. Das wäre aber KEIN MUSS. Auch wäre es gut wenn man das ,,Wein' bei unserem Namen weglassen könnte.
Das Etikett sollte aus Vorder-und Rückenetikett bestehen und edel wirken. Vorne sollte die Rebsorte und die Geschmacksangabe stehen. Der Rest sollte auf das Rückenetikett.
Das Vorderetikett sollte ein richtiger Eyecatcher sein und im Supermarkt z.B. aus vielen anderen herausstechen. Das wäre ganz wichtig.
Man kann bei den Farben unterscheiden in 3 Konzepte.
Literwein als einsteiger Wein
Dann die Gutsweine und zum Schluss die Lagenweine. Alles Farblich oder im design etwas abgesetzt.

```html
<!DOCTYPE html>
<html lang="de">
<head>
<meta charset="utf-8">
<title>Brunnhofer – Hausetikett</title>
<link rel="stylesheet" href="https://fonts.googleapis.com/css2?family=Bodoni+Moda:wght@500&family=Roboto+Condensed:wght@300;400;700&display=swap">
<style>
  :root {
    --stage: #d9d9d9;
    --paper: #f3f3f3;
    --ink: #111111;
    --night: #0b0b0b;
    --copper: #b9825a;
    --text-light: #e6e6e6;
  }
  * { margin: 0; padding: 0; box-sizing: border-box; }
  html, body {
    width: 1200px; height: 1147px; overflow: hidden;
    background: radial-gradient(ellipse at center, #f2f2f2 0%, var(--stage) 75%);
  }
  .label-set {
    position: absolute; left: 45px; top: 293px;
    display: flex; gap: 40px; align-items: center;
  }
  .label {
    position: relative; width: 350px; height: 560px; overflow: hidden;
    box-shadow: 0 6px 22px rgba(0,0,0,.22);
  }
  .label--literwein { background: var(--paper); color: var(--ink); }
  .label--lagenwein { background: var(--night); color: var(--copper); }
  .label--back { width: 330px; height: 530px; background: var(--night); color: var(--text-light); text-align: center; }

  .label__pattern { position: absolute; inset: 0; width: 100%; height: 100%; }
  .label__mark {
    position: absolute; left: 50%; top: 280px; width: 40px; height: 40px;
    margin: -20px 0 0 -20px; border-radius: 50%;
  }
  .label--literwein .label__mark { background: var(--ink); }
  .label--lagenwein .label__mark { background: #ffffff; }

  .label__line {
    position: absolute; left: 0; right: 0; top: 478px; text-align: center;
    font: 400 15px/1 "Roboto Condensed", sans-serif; letter-spacing: 1.5px; text-transform: uppercase;
  }
  .label--lagenwein .label__line { color: var(--text-light); font-weight: 300; }
  .label__name {
    position: absolute; left: 0; right: 0; top: 500px; text-align: center;
    font: 500 44px/1 "Bodoni Moda", serif; letter-spacing: 1px; text-transform: uppercase;
  }

  .back__mark {
    position: absolute; left: 50%; top: 40px; width: 34px; height: 34px;
    margin-left: -17px; border-radius: 50%; background: var(--copper);
  }
  .back__name {
    position: absolute; left: 0; right: 0; top: 88px;
    font: 500 34px/1 "Bodoni Moda", serif; color: var(--copper); text-transform: uppercase; letter-spacing: .5px;
  }
  .back__text {
    position: absolute; left: 0; right: 0;
    font: 300 15px/1.35 "Roboto Condensed", sans-serif;
  }
  .back__wine { top: 178px; }
  .back__quality { top: 244px; }
  .back__legal { top: 286px; }
  .back__volume {
    position: absolute; left: 0; right: 0; top: 414px;
    display: flex; justify-content: center; gap: 36px;
    font: 300 15px/1 "Roboto Condensed", sans-serif;
  }
  .back__estate {
    position: absolute; left: 0; right: 0; top: 474px;
    font: 700 11px/1.5 "Roboto Condensed", sans-serif; text-transform: uppercase;
  }
  .back__address { font-weight: 300; text-transform: none; font-size: 11px; }
</style>
</head>
<body>
  <main class="label-set">
    <section class="label label--literwein">
      <svg class="label__pattern" viewBox="0 0 350 560" role="img" aria-label="Geometrisches Kreisornament in Grau, diagonal angeschnitten">
        <defs>
          <linearGradient id="grey-ornament" x1="0" y1="0" x2="1" y2="1">
            <stop offset="0" stop-color="#6f6f6f"/>
            <stop offset="1" stop-color="#b5b5b5"/>
          </linearGradient>
        </defs>
        <polygon points="0,0 350,0 350,50 0,310" fill="url(#grey-ornament)"/>
      </svg>
      <span class="label__mark"></span>
      <p class="label__line">Literwein &nbsp;-&nbsp; 2019 &nbsp;-&nbsp; Geschmack</p>
      <h2 class="label__name">Brunnhofer</h2>
    </section>

    <section class="label label--lagenwein">
      <svg class="label__pattern" viewBox="0 0 350 560" role="img" aria-label="Geometrisches Kreisornament in Kupfer, diagonal angeschnitten">
        <defs>
          <linearGradient id="copper-ornament" x1="0" y1="0" x2="1" y2="1">
            <stop offset="0" stop-color="#c08a5f"/>
            <stop offset="1" stop-color="#6e4a30"/>
          </linearGradient>
        </defs>
        <polygon points="0,0 350,0 350,50 0,310" fill="url(#copper-ornament)"/>
      </svg>
      <span class="label__mark"></span>
      <p class="label__line">Lagenwein &nbsp;-&nbsp; 2019 &nbsp;-&nbsp; Geschmack</p>
      <h2 class="label__name">Brunnhofer</h2>
    </section>

    <section class="label label--back">
      <span class="back__mark"></span>
      <h2 class="back__name">Brunnhofer</h2>
      <p class="back__text back__wine">Gewürztraminer<br>Rebenheimer Sonnenhang</p>
      <p class="back__text back__quality">Deutscher Qualitätswein</p>
      <p class="back__text back__legal">A. P. Nr. 1 234 567 890 12<br>Enthält Sulfite<br>Erzeugerabfüllung</p>
      <p class="back__volume"><span>℮ 750 ml</span><span>11,5% Vol.</span></p>
      <p class="back__estate">Weingut Brunnhofer<br><span class="back__address">Lindenweg 14 · 55555 Rebenheim · Tel. 01234 - 000 00</span></p>
    </section>
  </main>
</body>
</html>
```